Revamp Current Website From 2012 TO 2018

We need a ravamp to our current website. I prefer a professional corporate modern feel to it.

My Current Website is www.brightlanepromoworks.biz. Please redesign the homepage and the /certs page first....see attached document for specific instructions..

There is a lot of content at the bottom but maybe we can shorten that by using titles and a pop up of the details or something so it doesnt take too mcuh space...or maybe a red more hyperlink to see the rest of info in pop up or something or new page...

Target Market(s)

B2B, business owners, website owners, marketing companies.

Industry/Entity Type

Promotional Product

Number of Pages Required

2 page

Colors

Designer to choose colors to be used in the design.

Requirements
Must have
• Please keep in mind logo mock up I am working on that looks beautiful on dark background for header...see attached for logo
• Must use existing content I hope your marketing mind comes in to play when designing the website.
• Must have all my content provided on each page...
Nice to have
• similiar color scheme...
Should not have
• I dont like using templates because usually hard to expand on design in future so Prefer full custom designs
• Please no templates

```html
<!DOCTYPE html>
<html lang="en">
<head>
<meta charset="utf-8">
<title>Bright Lane Promo Works – Unlimited Incentives</title>
<link href="https://fonts.googleapis.com/css2?family=Arimo:wght@400;700&display=swap" rel="stylesheet">
<style>
:root{
  --blue:#2a9fe0;
  --blue-dark:#1b8fd0;
  --slate:#5a86a6;
  --navy:#1a2b4c;
  --red:#c8262c;
  --grey-band:#d6d6d6;
  --nav-grey:#9a9a9a;
  --ink:#111;
  --white:#fff;
}
*{box-sizing:border-box;margin:0;padding:0}
html,body{width:1200px;height:5373px;overflow:hidden}
body{font-family:"Arimo",Arial,sans-serif;color:var(--ink);background:var(--white);position:relative}
.abs{position:absolute}

/* nav */
.topnav{top:0;left:0;width:1200px;height:50px;background:var(--nav-grey);display:flex;align-items:center;padding-left:14px}
.topnav a{color:var(--white);text-decoration:none;font-size:20px;padding:0 12px;height:50px;line-height:50px;white-space:nowrap}
.topnav a.current{background:var(--white);color:var(--ink)}
.topnav a.login{background:#111;height:36px;line-height:36px;margin-left:6px}

/* header */
.masthead{top:50px;left:0;width:1200px;height:165px}
.brand{left:36px;top:42px;display:flex;align-items:center;gap:14px}
.brand-dot{width:80px;height:80px;border-radius:50%;background:var(--navy)}
.brand-name{font-size:58px;font-weight:700;color:var(--navy)}
.contact{left:478px;top:52px;display:flex;gap:22px;align-items:flex-start}
.contact p{font-size:21px;line-height:26px}
.offer{right:34px;top:36px;text-align:right;font-size:21px;line-height:26px}
.offer strong{font-size:25px;display:block}

/* hero */
.hero{top:215px;left:0;width:1200px;height:662px;background:linear-gradient(90deg,#8c8c8c 0%,#d8d8d8 40%,#ececec 70%,#bdbdbd 100%)}
.hero-art{top:0;left:0;width:1200px;height:662px}
.hero h1{left:40px;top:170px;font-size:54px;line-height:62px;font-weight:700;color:#111}
.btn-red{left:46px;top:418px;width:224px;height:56px;background:var(--red);color:var(--white);font-size:21px;font-weight:700;display:flex;align-items:center;justify-content:center}

/* ways */
.section-title{width:1200px;left:0;text-align:center;font-weight:700}
.ways-title{top:960px;font-size:52px;color:var(--blue)}
.way{top:1130px;width:340px}
.way h3{font-size:30px;font-weight:700;margin:26px 0 14px;line-height:32px}
.way p{font-size:20px;line-height:26px}

/* plug in */
.plug{top:1610px;left:0;width:1200px;height:717px;background:var(--blue);color:var(--white)}
.plug h2{position:absolute;top:85px;width:1200px;text-align:center;font-size:42px;font-weight:700}
.plug-item{position:absolute}
.plug-item.col-left{left:46px;width:555px}
.plug-item.col-right{left:680px;width:420px}
.plug-item h4{font-size:23px;margin-bottom:18px}
.plug-item p{font-size:19px;line-height:25px}

/* clients */
.clients-title{top:2455px;font-size:44px;color:#111}
.client{top:2585px;width:258px;height:170px;background:#cfd3d6;border-radius:8px;padding:12px}
.client div{width:100%;height:100%;background:var(--white);display:flex;align-items:center;justify-content:center;font-size:28px;font-weight:700;color:var(--navy)}

/* video */
.video-band{top:2900px;left:0;width:1200px;height:680px;background:var(--grey-band)}
.video-band h2{position:absolute;top:78px;width:1200px;text-align:center;font-size:46px;font-weight:700}
.video-band h3{position:absolute;top:140px;width:1200px;text-align:center;font-size:34px;font-weight:700}
.video-band h3 span{color:var(--red);font-size:42px}
.player{left:333px;top:225px;width:547px;height:330px;background:#000;border:6px solid var(--blue)}

/* brochure */
.brochure{top:3650px;font-size:44px}
.brochure span{color:var(--red)}

/* split */
.split-photo{top:3802px;left:0;width:609px;height:716px;background:linear-gradient(135deg,#cfd4d8 0%,#8e9aa5 45%,#3c4b5b 100%)}
.split-panel{top:3802px;left:609px;width:591px;height:716px;background:var(--slate);color:var(--white);text-align:center}
.split-panel h2{margin-top:140px;font-size:42px;line-height:52px;font-weight:700;padding:0 95px}
.btn-outline{display:inline-block;margin-top:60px;border:3px solid var(--white);border-radius:6px;padding:18px 36px;font-size:22px}

/* signup */
.signup{top:4518px;left:0;width:1200px;height:619px;background:var(--blue)}
.signup h2{position:absolute;top:100px;width:1200px;text-align:center;color:var(--white);font-size:42px;font-weight:700}
.field{position:absolute;left:333px;width:519px;height:58px;background:var(--white);font-size:30px;padding-left:14px;line-height:58px;color:#222}
.field.cta{background:#000;color:var(--white);text-align:center;padding:0}

/* footer */
.footer{top:5137px;left:0;width:1200px;height:236px}
.footer p{position:absolute;left:40px;font-size:20px;line-height:27px}
.footer .brand{left:auto;right:40px;top:60px}
.footer .brand-dot{width:62px;height:62px}
.footer .brand-name{font-size:44px}
</style>
</head>
<body>

<nav class="abs topnav">
  <a class="current">HOME</a><a>OUR INCENTIVES</a><a>SAMPLES</a><a>HOW IT WORKS</a><a>TESTIMONIALS</a><a>FAQ</a><a>CONTACT</a><a class="login">LOG IN</a>
</nav>

<header class="abs masthead">
  <div class="abs brand"><span class="brand-dot"></span><span class="brand-name">BLPW</span></div>
  <div class="abs contact">
    <svg width="30" height="56" viewBox="0 0 30 56"><rect x="2" y="2" width="26" height="52" rx="4" fill="#222"/><rect x="6" y="8" width="18" height="34" fill="#fff"/><circle cx="15" cy="48" r="3" fill="#fff"/></svg>
    <p>USA Office: 555-214-7380<br>International: 1-800-555-0142</p>
  </div>
  <div class="abs offer">Unlimited Incentives<br>For $99 Monthly - No Contracts<br>30 Day Risk Free Trial<strong>SIGN UP RIGHT NOW</strong></div>
</header>

<section class="abs hero">
  <div class="abs hero-art" role="img" aria-label="Businessman in a suit leaping up, holding a rising red chart arrow drawn on a concrete wall"></div>
  <h1 class="abs">Give Away<br>Unlimited Incentives<br>To Your Customers</h1>
  <div class="abs btn-red">LEARN MORE</div>
</section>

<h2 class="abs section-title ways-title">Three Easy Ways!</h2>
<div class="abs way" style="left:40px">
  <svg width="76" height="76" viewBox="0 0 76 76"><rect x="18" y="4" width="40" height="22" fill="none" stroke="#222" stroke-width="5"/><rect x="4" y="26" width="68" height="30" rx="4" fill="#222"/><rect x="18" y="46" width="40" height="26" fill="#fff" stroke="#222" stroke-width="5"/></svg>
  <h3>PRINT</h3>
  <p>Download PDF Certificates to print and hand them out or mail them to your customers!</p>
</div>
<div class="abs way" style="left:424px">
  <svg width="90" height="76" viewBox="0 0 90 76"><path d="M5 30 L45 4 L85 30 V72 H5Z" fill="#222"/><rect x="18" y="16" width="54" height="40" fill="#fff"/><text x="45" y="46" text-anchor="middle" font-size="26" font-family="Arimo,Arial,sans-serif" font-weight="700" fill="#222">@</text><path d="M5 30 L45 58 L85 30 V72 H5Z" fill="#222"/></svg>
  <h3>E-MAIL</h3>
  <p>Email E-Certificates to your customers with one click!</p>
</div>
<div class="abs way" style="left:834px">
  <svg width="76" height="80" viewBox="0 0 76 80"><rect x="6" y="4" width="38" height="68" rx="5" fill="none" stroke="#222" stroke-width="5"/><rect x="14" y="14" width="22" height="40" fill="none" stroke="#222" stroke-width="3"/><path d="M40 40 l8 26 6-8 10 12 5-4 -10-12 9-4z" fill="#222"/></svg>
  <h3>FROM YOUR<br>WEBSITE</h3>
  <p>Place our HTML banners on your homepage. Your customers click on the banner to get their Certificate. We email you their contact information - 100% Lead Generation Automation!</p>
</div>

<section class="abs plug">
  <h2>How BLPW Plugs Into Your Business Model</h2>
  <div class="plug-item col-left" style="top:180px"><h4>Advertising</h4><p>Boost response rates from your existing ads by adding one extra tagline: "Call for a Free Quote and receive a Three Day Two Night Hotel Stay Certificate to Las Vegas or 50 + other popular destinations. No Purchase Necessary." Imagine how many more leads you could generate.</p></div>
  <div class="plug-item col-right" style="top:180px"><h4>Sales</h4><p>Now that you have generated the lead, try enticing a prospect with an upgrade and offer them Two Nights Plus Airfare if they purchase today. There are so many ways to clinch a deal by offering our incentives as a reward in your closing question.</p></div>
  <div class="plug-item col-left" style="top:430px"><h4>Residual Business</h4><p>Remind past clients about your products &amp; services with a 2 Night Mini of your previous business clients using a personal touch and an incentive to boot.</p></div>
  <div class="plug-item col-right" style="top:430px"><h4>Referrals</h4><p>Contact all of your past customers and offer a Deluxe Vacation Package to anyone who fulfills your request for a new referral. Or, at the end of your sales presentation, after you have achieved the sale, seduce new clients with a tempting perk if they send you a referral.</p></div>
</section>

<h2 class="abs section-title clients-title">Our Clients</h2>
<div class="abs client" style="left:64px"><div>Harborline</div></div>
<div class="abs client" style="left:348px"><div>ValueDirect</div></div>
<div class="abs client" style="left:612px"><div>Norvale</div></div>
<div class="abs client" style="left:886px"><div>Skycast</div></div>

<section class="abs video-band">
  <h2>Watch Video</h2>
  <h3>to Save <span>20%</span> Today</h3>
  <div class="abs player">
    <svg width="535" height="318" viewBox="0 0 535 318"><circle cx="267" cy="145" r="16" fill="#555"/><path d="M262 137 L274 145 L262 153Z" fill="#ccc"/><rect x="0" y="292" width="535" height="26" fill="#d9d9d9"/><rect x="40" y="302" width="380" height="6" fill="#888"/><rect x="40" y="302" width="170" height="6" fill="#333"/><path d="M12 298 l10 7 -10 7z" fill="#333"/></svg>
  </div>
</section>

<h2 class="abs section-title brochure">View Our <span>ONLINE BROCHURE</span></h2>

<div class="abs split-photo" role="img" aria-label="Two businesspeople shaking hands, one in a grey sweater and one in a suit and tie"></div>
<section class="abs split-panel">
  <h2>Know Any Businesses That Could Benefit Using Incentives To Bring In More Customers?</h2>
  <span class="btn-outline">LEARN MORE</span>
</section>

<section class="abs signup">
  <h2>SIGN UP RISK-FREE FOR 30 DAYS</h2>
  <div class="field" style="top:200px">NAME</div>
  <div class="field" style="top:272px">EMAIL</div>
  <div class="field" style="top:344px">PHONE</div>
  <div class="field" style="top:416px">USERNAME</div>
  <div class="field cta" style="top:490px">TRY FOR 30 DAYS</div>
</section>

<footer class="abs footer">
  <p style="top:52px">© 2005-2014 Bright Lane Promo Works, Inc. -<br>All Rights Reserved</p>
  <p style="top:112px">Affiliate Program | Terms &amp; Conditions | Privacy Policy |</p>
  <div class="abs brand"><span class="brand-dot"></span><span class="brand-name">BLPW</span></div>
</footer>

</body>
</html>
```